Professional Corporate Christmas Card

We require a Christmas card to send to corporate clients on behalf of our Accounting and Financial planning firm.
We like a clean design and our corporate colours are white, blue and silvery grey.
We don't want our logo on the front of the card. We would like something professional and elegant on the front, with the message 'Merry Christmas' or similar.
Our text for the inside of the card is:
Our very best wishes to you this festive season.
May 2014 bring you peace, joy and prosperity.
From the Directors and Staff at Dunmore Group of Companies.
We would like our logo to be subtly placed within the inside of the card - it could have a level of transparency if that helps to gain that effect. It could also be built into the design if you wish. I have attached the logo.
Our website is at http://dunmoregroup-example.com.au/ to give an idea of our corporate style.
**We will be printing through Printlane, so we would like the colours you use to be CYMK**
We will order the card size - 182x117cm (folded)
Thank you for considering the proposal ... we look forward to receiving your designs!
Target Market(s)
The audience of this card is varied: property developers, CEO's, cane farmers, professionals - it will be going to referral sources and our top end clients.
Industry/Entity Type
Printing

```html
<!DOCTYPE html>
<html lang="en">
<head>
<meta charset="utf-8">
<title>Dunmore Group of Companies – Christmas Card</title>
<link rel="stylesheet" href="https://fonts.googleapis.com/css2?family=Nunito:wght@800;900&display=swap">
<style>
  :root {
    --brand-blue: #2f80fb;
    --frame-silver: #dde3e6;
    --glow-blue: #c9dcfb;
    --paper: #ffffff;
    --snow: rgba(236, 242, 248, 0.78);
  }
  * { margin: 0; padding: 0; box-sizing: border-box; }
  html, body {
    width: 1200px; height: 771px; overflow: hidden;
    background: var(--paper);
    font-family: "Nunito", "Arial Rounded MT Bold", sans-serif;
  }
  .canvas { position: relative; width: 1200px; height: 771px; }

  /* Front cover */
  .card-front {
    position: absolute; left: 0; top: 0; width: 600px; height: 771px;
    background: var(--brand-blue);
  }
  .card-front__frame {
    position: absolute; left: 18px; top: 18px; width: 566px; height: 738px;
    background: var(--frame-silver);
  }
  .card-front__field {
    position: absolute; left: 32px; top: 32px; width: 538px; height: 710px;
    background: radial-gradient(ellipse 260px 360px at 250px 350px, var(--glow-blue) 0%, #8fb8fb 45%, var(--brand-blue) 100%);
  }
  .greeting {
    position: absolute;
    transform: translate(-50%, -50%) rotate(-90deg);
    white-space: nowrap;
    font-weight: 900;
    color: var(--snow);
    line-height: 1;
    text-transform: uppercase;
  }
  .greeting--merry { left: 242px; top: 392px; font-size: 96px; letter-spacing: 2px; }
  .greeting--christmas { left: 367px; top: 400px; font-size: 100px; letter-spacing: 1px; }

  /* Inside page */
  .card-inside {
    position: absolute; left: 618px; top: 15px; width: 567px; height: 741px;
    background: var(--brand-blue);
  }
  .card-inside__page {
    position: absolute; left: 15px; top: 17px; width: 535px; height: 708px;
    background: var(--paper);
  }
  .rotated {
    position: absolute;
    transform: translate(-50%, -50%) rotate(-90deg);
    white-space: nowrap;
    color: var(--brand-blue);
    line-height: 1;
  }
  .message { font-weight: 900; font-size: 23.5px; letter-spacing: 0.4px; }
  .message--wishes { left: 830px; top: 387px; }
  .message--new-year { left: 876px; top: 388px; }
  .sign-off { left: 975px; top: 390px; font-weight: 900; font-size: 15px; letter-spacing: 0.2px; }

  .brand-mark { left: 1084px; top: 390px; display: flex; align-items: center; gap: 8px; }
  .brand-mark__dot {
    width: 18px; height: 18px; border-radius: 50%;
    background: var(--brand-blue);
  }
  .brand-mark__name { font-weight: 900; font-size: 26px; color: var(--brand-blue); }
</style>
</head>
<body>
<main class="canvas">
  <section class="card-front" aria-label="Card front">
    <div class="card-front__frame"></div>
    <div class="card-front__field"></div>
    <p class="greeting greeting--merry">Merry</p>
    <p class="greeting greeting--christmas">Christmas</p>
  </section>

  <section class="card-inside" aria-label="Card inside">
    <div class="card-inside__page"></div>
  </section>
  <p class="rotated message message--wishes">Our very best wishes to you this festive season.</p>
  <p class="rotated message message--new-year">May 2014 bring you peace, joy and prosperity</p>
  <p class="rotated sign-off">From the Directors and Staff at Dunmore Group of Companies.</p>
  <div class="rotated brand-mark">
    <span class="brand-mark__dot"></span>
    <span class="brand-mark__name">Dunmore</span>
  </div>
</main>
</body>
</html>
```